Executive to COACH PPT needs Power Point Design

I would like a powerpoint showing the words executive morphing into the word coach. There is an example attached with the word women morphing into the word coach. It can be done the same way. i am not concerned about the color or the font. It should take the same number of slides to create the morph. I would like the word to take up a large part of the powerpoint page.

I think the attachment should help you understand exactly what i am looking for. I would like it with the same number of powerpoint slides.

The purpose of these powerpoints is for an executive to see this and to understand that if they are going to succeed as an executive they need to morph into a coach. we spend three days teaching them how to do that.

Target Market(s)

executives that are participating in a workshop to be held around the world.

Font styles to use
Sans Serif

Requirements
Must have
• clear beginning with the word EXECUTIVE, clear ending with the word COACH. the look has to be modern and worldly. it has to be international in its feel.
Nice to have
• great color, attractive font and a real connectivity with the words. Making sure the reader understands exactly what we are trying to do.
Should not have
• drawings or designs other than the words, no extra fuss anywhere other than the words.

```html
<!DOCTYPE html>
<html lang="en">
<head>
<meta charset="UTF-8">
<title>Executive to Coach – Morph Slides</title>
<link href="https://fonts.googleapis.com/css2?family=Arimo:wght@700&display=swap" rel="stylesheet">
<style>
  :root {
    --page-bg: #ffffff;
    --bg-orange: #ff9a0a;
    --bg-olive: #b9c40e;
    --bg-green: #3ef53a;
    --bg-mint: #3df7a8;
    --bg-cyan: #20f0f4;
    --bg-sky: #8fbcff;
    --bg-lavender: #b596ff;
    --gold-light: #f5c44a;
    --gold-mid: #c98a14;
    --gold-deep: #7a4806;
    --ink-dark: #14102a;
    --shadow: rgba(20, 15, 40, 0.55);
  }
  * { margin: 0; padding: 0; box-sizing: border-box; }
  html, body {
    width: 960px;
    height: 1200px;
    overflow: hidden;
    background: var(--page-bg);
  }
  .sheet {
    position: relative;
    width: 960px;
    height: 1200px;
  }
  .slide {
    position: absolute;
    width: 444px;
    height: 332px;
    overflow: hidden;
    background:
      radial-gradient(ellipse at 30% 20%, rgba(255,255,255,0.18), transparent 60%),
      radial-gradient(ellipse at 70% 80%, rgba(255,255,255,0.14), transparent 55%),
      linear-gradient(90deg, var(--bg-orange) 0%, var(--bg-olive) 18%, var(--bg-green) 40%, var(--bg-mint) 55%, var(--bg-cyan) 66%, var(--bg-sky) 82%, var(--bg-lavender) 100%);
  }
  .col-left { left: 26px; }
  .col-right { left: 490px; }
  .row-1 { top: 117px; }
  .row-2 { top: 467px; }
  .row-3 { top: 816px; }

  .word, .finale .line {
    position: absolute;
    left: 0;
    right: 0;
    text-align: center;
    font-family: "Arimo", Arial, sans-serif;
    font-weight: 700;
    font-size: 64px;
    line-height: 1;
    letter-spacing: -1.5px;
    white-space: nowrap;
  }
  .word {
    top: 50%;
    transform: translateY(-50%);
  }
  .gold, .dark {
    display: inline-block;
    filter: drop-shadow(3px 4px 3px var(--shadow));
  }
  .gold {
    background: linear-gradient(160deg, var(--gold-light) 0%, var(--gold-mid) 40%, var(--gold-deep) 70%, var(--gold-light) 100%);
    -webkit-background-clip: text;
    background-clip: text;
    color: transparent;
  }
  .dark { color: var(--ink-dark); }

  .finale .line-top { top: 104px; }
  .finale .line-bottom { top: 176px; }
</style>
</head>
<body>
  <main class="sheet">
    <section class="slide col-left row-1">
      <p class="word"><span class="gold">EXECUTIVE</span></p>
    </section>

    <section class="slide col-right row-1">
      <p class="word"><span class="gold">CO</span><span class="dark">TIV</span></p>
    </section>

    <section class="slide col-left row-2">
      <p class="word"><span class="gold">COA</span><span class="dark">IV</span></p>
    </section>

    <section class="slide col-right row-2">
      <p class="word"><span class="gold">COAC</span><span class="dark">V</span></p>
    </section>

    <section class="slide col-left row-3">
      <p class="word"><span class="gold">COACH</span></p>
    </section>

    <section class="slide col-right row-3 finale">
      <p class="line line-top"><span class="gold">EXECUTIVE</span></p>
      <p class="line line-bottom"><span class="gold">COACH</span></p>
    </section>
  </main>
</body>
</html>
```